Grey orchard secret

UPDATED BRIEF:
I'm just updating the brief to enable any new submissions to come up with their own ideas. I have tried to offer my ideas below, but I am too close to the project therefor any new submissions are probably best using your talent. The main thing is it stands out and someone would want to buy it against the competition. All submissions have been excellent, so to be fair I will put the winning vote to family and friends. I am too close and biased to make the final choice.
This book is part memoire/ part biography/ part diary/ part self help.
My world is falling apart. I use the analogy of being lost at see. This book is my ships log. It could be a torn out PAGE of the log, a POSTER, or A MESSAGE a bottle.
It needs to be clear in the title, so GREY ORCHARD SECRET needs to stand out. BOO could be a wax seal, like a stamp. 'You've found the' and 'We're dancing at dusk' are less important. The title is: BOO You've found the GREY ORCHARD SECRET We're dancing at dusk.
Other subliminal random words are: family, paranoia, sex addiction, depression, marriage, divorce.
The other idea is flame red. Needs to be subtle to show my life is going up in flames. The diary page/poster/note should be singed or worn.
Ideally text font should be bespoke. Whether some or all are slightly wonky to show that my life is falling apart.
Octopus bottom left with tentacles spread over spine is a firm favourite
Text on spine needs to be large to stand out. Open to suggestions but nothing over simple.Good luck

Target Market(s)

30-60 years

Colors

Requirements
Must have
• Book size. I'm assuming: 21.5cm x 13.5cm x 2.5cm. I will need ebook version and paperback version. ISBN details will follow later

```html
<!DOCTYPE html>
<html lang="en">
<head>
<meta charset="utf-8">
<title>Grey Orchard Secret — Book Cover</title>
<link rel="stylesheet" href="https://fonts.googleapis.com/css2?family=Bebas+Neue&family=Caveat:wght@500&family=Montserrat:wght@500&display=swap">
<style>
  :root {
    --cover-red: #e01b22;
    --ink: #111111;
    --paper: #ffffff;
    --flame-core: #ffe15a;
    --flame-mid: #ffa31a;
    --flame-edge: rgba(224, 27, 34, 0);
  }
  * { margin: 0; padding: 0; box-sizing: border-box; }
  html, body { width: 777px; height: 1200px; overflow: hidden; background: var(--cover-red); }
  .cover {
    position: relative;
    width: 777px;
    height: 1200px;
    background: var(--cover-red);
    overflow: hidden;
  }
  .series-line {
    position: absolute;
    top: 70px; left: 0; width: 100%;
    text-align: center;
    font-family: "Bebas Neue", "Arial Narrow", sans-serif;
    font-size: 82px;
    line-height: 1;
    color: var(--paper);
    white-space: nowrap;
  }
  .theme-word {
    position: absolute;
    font-family: "Caveat", cursive;
    font-size: 36px;
    line-height: 1;
    color: var(--ink);
    white-space: nowrap;
    transform-origin: left center;
  }
  .theme-paranoia  { left: 66px;  top: 186px; transform: rotate(14deg); }
  .theme-sex       { left: 106px; top: 282px; transform: rotate(-24deg); }
  .theme-addiction { left: 62px;  top: 378px; transform: rotate(-34deg); }
  .theme-divorce   { left: 586px; top: 236px; transform: rotate(-22deg); }
  .theme-family    { left: 626px; top: 268px; transform: rotate(22deg); }
  .theme-menopause { left: 588px; top: 302px; transform: rotate(34deg); }

  .label-box {
    position: absolute;
    left: 214px; top: 196px;
    width: 350px; height: 168px;
    border: 6px solid var(--ink);
    border-radius: 18px;
    transform: rotate(-2deg);
    display: flex; align-items: center; justify-content: center;
  }
  .label-word {
    font-family: "Bebas Neue", "Arial Narrow", sans-serif;
    font-size: 150px;
    line-height: 1;
    color: var(--ink);
    letter-spacing: 0.04em;
    padding-top: 10px;
  }

  .kicker {
    position: absolute;
    top: 416px; left: 96px; right: 96px;
    display: flex; align-items: center; gap: 14px;
    font-family: "Montserrat", "Helvetica Neue", sans-serif;
    font-weight: 500;
    font-size: 44px;
    line-height: 1;
    color: var(--ink);
    text-transform: uppercase;
    white-space: nowrap;
  }
  .kicker::before, .kicker::after {
    content: "";
    flex: 1;
    height: 3px;
    background: var(--ink);
  }

  .flames {
    position: absolute;
    left: -20px; top: 570px;
    width: 817px; height: 300px;
    background:
      radial-gradient(ellipse 36% 30% at 52% 50%, var(--flame-core) 0%, rgba(255, 225, 90, 0) 100%),
      radial-gradient(ellipse 55% 42% at 48% 52%, var(--flame-mid) 0%, rgba(255, 163, 26, 0.6) 40%, var(--flame-edge) 100%);
  }

  .title {
    position: absolute;
    top: 482px; left: 0; width: 100%;
    text-align: center;
    font-family: "Bebas Neue", "Arial Narrow", sans-serif;
    font-weight: 400;
    color: var(--paper);
    line-height: 0.82;
  }
  .title-line { display: block; white-space: nowrap; }
  .title-line--upper { font-size: 150px; }
  .title-line--lower { font-size: 292px; margin-top: 12px; }

  .tagline {
    position: absolute;
    top: 910px; left: 0; width: 100%;
    text-align: center;
    font-family: "Montserrat", "Helvetica Neue", sans-serif;
    font-weight: 500;
    font-size: 48px;
    line-height: 1;
    color: var(--ink);
    text-transform: uppercase;
    white-space: nowrap;
  }

  .author {
    position: absolute;
    top: 1058px; left: 0; width: 100%;
    text-align: center;
    font-family: "Bebas Neue", "Arial Narrow", sans-serif;
    font-size: 76px;
    line-height: 1;
    color: var(--paper);
    letter-spacing: 0.2em;
    padding-left: 0.2em;
  }
</style>
</head>
<body>
<main class="cover">
  <div class="series-line">Notes From A Tired Father</div>

  <span class="theme-word theme-paranoia">Paranoia</span>
  <span class="theme-word theme-sex">Sex</span>
  <span class="theme-word theme-addiction">Addiction</span>
  <span class="theme-word theme-divorce">Divorce</span>
  <span class="theme-word theme-family">Family</span>
  <span class="theme-word theme-menopause">Menopause</span>

  <div class="label-box">
    <span class="label-word">BOO</span>
  </div>

  <h2 class="kicker">You've found the</h2>

  <div class="flames" role="img" aria-label="Flames licking across the title, showing a life going up in fire"></div>

  <h1 class="title">
    <span class="title-line title-line--upper">Grey Orchard</span>
    <span class="title-line title-line--lower">Secret</span>
  </h1>

  <p class="tagline">We're dancing at dusk</p>

  <p class="author">Miles Farrow</p>
</main>
</body>
</html>
```